Software company specialized in data analytics and professional services

We need a landing page design for our business. It should include our logo design. It should have multiple sections :
- stylish head
- what we do (data analytics software, professional services)
- contact form

Target Market(s)

Companies, B2B

Industry/Entity Type

Data

Number of Pages Required

1 page

Font styles to use
Sans Serif

Requirements
Must have
• Dark theme
Should not have
• Gradients on buttons

```html
<!DOCTYPE html>
<html lang="en">
<head>
<meta charset="utf-8">
<title>Northgrid — Empowering Growth</title>
<link href="https://fonts.googleapis.com/css2?family=Arimo:wght@400;700&display=swap" rel="stylesheet">
<style>
  :root{
    --ink:#ffffff;
    --bg:#000000;
    --teal:rgba(16,122,115,0.95);
    --maroon:rgba(98,38,52,0.95);
    --moss:rgba(62,92,68,0.9);
    --card:#544b74;
    --panel:#0c0c0c;
    --footer:#0f0f0f;
    --brand:#b0179f;
    --field-border:#c9c9c9;
    --placeholder:#8a8a8a;
    --button:#f2f2f2;
  }
  *{box-sizing:border-box;margin:0;padding:0}
  html,body{width:1200px;height:2211px;overflow:hidden}
  body{
    position:relative;
    font-family:"Arimo",Arial,sans-serif;
    color:var(--ink);
    background:
      radial-gradient(circle 300px at 960px 210px,var(--teal),transparent),
      radial-gradient(circle 330px at 110px 580px,var(--maroon),transparent),
      radial-gradient(circle 260px at 1240px 820px,var(--moss),transparent),
      radial-gradient(circle 330px at 140px 1140px,var(--teal),transparent),
      radial-gradient(circle 330px at 880px 1640px,var(--moss),transparent),
      radial-gradient(circle 280px at 120px 2120px,rgba(16,122,115,0.7),transparent),
      var(--bg);
  }
  .abs{position:absolute}
  .brand{font-weight:700;color:var(--brand);letter-spacing:0.5px}
  .site-header .brand{left:87px;top:27px;font-size:20px}
  .nav a{position:absolute;top:34px;font-size:13px;color:var(--ink);text-decoration:none}
  .hero-title{left:0;width:1200px;top:140px;text-align:center;font-size:78px;line-height:90px;font-weight:400}
  .hero-lead{left:310px;width:580px;top:370px;text-align:center;font-size:16px;line-height:20px}
  .cta{left:523px;top:468px;width:154px;height:35px;border-radius:18px;background:var(--ink);color:#111;font-size:15px;display:flex;align-items:center;justify-content:center}
  .about-text{left:110px;width:980px;top:797px;text-align:center;font-size:38px;line-height:44px}
  .services-title{left:100px;top:1222px;font-size:74px;font-weight:700;line-height:88px}
  .service-card{top:1326px;width:279px;height:241px;background:var(--card);border-radius:9px}
  .service-card svg{position:absolute;left:22px;top:26px}
  .service-card h3{position:absolute;left:16px;top:146px;font-size:25px;font-weight:400}
  .testimonial-panel{left:73px;top:1836px;width:455px;height:259px;background:var(--panel);border-radius:8px}
  .testimonial{left:141px;top:1860px;width:318px;height:211px;background:#fff;border-radius:8px;color:#111;padding:22px 16px;font-size:15px;font-weight:700;line-height:18px}
  .testimonial cite{display:block;margin-top:14px;font-style:normal;font-size:16px}
  .contact-title{left:549px;top:1830px;font-size:53px;font-weight:700;line-height:60px}
  .field{height:41px;background:#fff;border:1px solid var(--field-border);color:var(--placeholder);font-size:15px;display:flex;align-items:center;justify-content:center;border-radius:2px}
  .send{left:553px;top:2059px;width:595px;height:45px;background:var(--button);color:#111;font-size:15px;display:flex;align-items:center;justify-content:center}
  .site-footer{left:0;top:2116px;width:1200px;height:95px;background:var(--footer);display:flex;align-items:center;justify-content:center}
  .site-footer .brand{font-size:40px}
</style>
</head>
<body>
  <header class="site-header">
    <div class="brand abs">NORTHGRID</div>
    <nav class="nav">
      <a href="#about" style="left:873px">About</a>
      <a href="#services" style="left:987px">Services</a>
      <a href="#contact" style="left:1117px">Contact</a>
    </nav>
  </header>

  <section class="hero">
    <h1 class="hero-title abs">EMPOWERING<br>GROWTH</h1>
    <p class="hero-lead abs">Lorem ipsum, dolor sit amet consectetur adipisicing elit. Quisquam distinctio provident quasi expedita sit a aspernatur unde est suscipit? Neque molestias porro veniam nisi?</p>
    <a class="cta abs">Get in Touch</a>
  </section>

  <section id="about">
    <p class="about-text abs">Lorem ipsum dolor sit amet, consectetur adipisicing elit. Omnis quos quas quia expedita dolorem nobis nemo quibusdam obcaecati, reprehenderit aliquid dolores odio laborum harum, nam corporis amet ducimus aut. Corrupti.</p>
  </section>

  <section id="services">
    <h2 class="services-title abs">Services</h2>
    <article class="service-card abs" style="left:9px">
      <svg width="54" height="52" viewBox="0 0 54 52" fill="none" stroke="#fff" stroke-width="1"><rect x="1" y="18" width="14" height="33" rx="3"/><rect x="20" y="1" width="14" height="50" rx="3"/><rect x="39" y="23" width="14" height="28" rx="3"/></svg>
      <h3>Data Analysis</h3>
    </article>
    <article class="service-card abs" style="left:304px">
      <svg width="54" height="52" viewBox="0 0 54 52" fill="none" stroke="#fff" stroke-width="1"><path d="M1 1V51H53"/><path d="M8 40L20 22L30 34L50 6"/><path d="M14 40L26 18L40 32L46 20"/></svg>
      <h3>Profesional Services</h3>
    </article>
    <article class="service-card abs" style="left:599px">
      <svg width="54" height="52" viewBox="0 0 54 52" fill="none" stroke="#fff" stroke-width="1"><rect x="1" y="18" width="14" height="33" rx="3"/><rect x="20" y="1" width="14" height="50" rx="3"/><rect x="39" y="23" width="14" height="28" rx="3"/></svg>
      <h3>Service 3</h3>
    </article>
    <article class="service-card abs" style="left:894px">
      <svg width="54" height="52" viewBox="0 0 54 52" fill="none" stroke="#fff" stroke-width="1"><path d="M1 1V51H53"/><path d="M8 40L20 22L30 34L50 6"/><path d="M14 40L26 18L40 32L46 20"/></svg>
      <h3>Service 4</h3>
    </article>
  </section>

  <section id="contact">
    <div class="testimonial-panel abs"></div>
    <blockquote class="testimonial abs">"Lorem ipsum dolor sit amet consectetur adipisicing elit. Ipsa nam corporis expedita porro minima, aliquam quo consequatur magnam debitis blanditiis impedit error eveniet provident fugit laboriosam exercitationem accusamus deleniti sunt."
      <cite>-John Doe</cite>
    </blockquote>
    <h2 class="contact-title abs">Lets Get in Touch!</h2>
    <div class="field abs" style="left:553px;top:1896px;width:290px">Your Name</div>
    <div class="field abs" style="left:853px;top:1896px;width:290px">Email</div>
    <div class="field abs" style="left:553px;top:1947px;width:290px">Phone</div>
    <div class="field abs" style="left:853px;top:1947px;width:290px">Subject</div>
    <div class="field abs" style="left:553px;top:1998px;width:587px;height:52px">Your Message</div>
    <div class="send abs">Send Message</div>
  </section>

  <footer class="site-footer abs">
    <div class="brand">NORTHGRID</div>
  </footer>
</body>
</html>
```